Corporate Powerpoint templates

I wish to have a standardized template for our manufacturing company. We manufacture baseball caps for major sport leagues and teams.
Our powerpoint should be clean, yet stylish.
We do a lot of presentations for technical trainings, KPI reports, quality assurance training.
We have factories in China, Bangladesh, and Mexico, so the look and feel must be internationally accepted.

Target Market(s)

Branded customers

Industry/Entity Type

Headwear Manufacturing

Font styles to use
Sans Serif

Colors
00AB8E
00BBA5
67D7C9
C6EFE9
E9F9F6

Requirements
Must have
• Spreadsheet slides, graphs, photographic reports
Nice to have
• Sporty, trendy, yet corporate feel.

```html
<!DOCTYPE html>
<html lang="en">
<head>
<meta charset="utf-8">
<title>Corporate Presentation Template</title>
<link href="https://fonts.googleapis.com/css2?family=Abril+Fatface&family=Josefin+Sans:wght@400;600&display=swap" rel="stylesheet">
<style>
  :root {
    --teal: #00ab8e;
    --teal-mid: #00bba5;
    --teal-light: #67d7c9;
    --teal-pale: #c6efe9;
    --teal-mist: #e9f9f6;
    --sand: #cbb68e;
    --brown: #9b6a55;
    --sienna: #8a4f3a;
    --charcoal: #4b4646;
    --slate: #7d7473;
    --ink: #111111;
    --text: #3d3d3d;
    --accent-red: #c8303a;
    --page: #ececec;
    --slide: #ffffff;
    --track: #e7e2d6;
    --map: #cfcfcf;
  }
  * { box-sizing: border-box; margin: 0; padding: 0; }
  html, body { width: 1200px; height: 4264px; overflow: hidden; background: var(--page); }
  body { font-family: "Josefin Sans", Arial, sans-serif; color: var(--text); position: relative; }
  .display { font-family: "Abril Fatface", Georgia, serif; font-weight: 400; }

  .slide {
    position: absolute; left: 40px; width: 1120px; height: 630px;
    background: var(--slide); overflow: hidden;
    box-shadow: 0 2px 10px rgba(0,0,0,.12);
  }
  .slide-1 { top: 40px; } .slide-2 { top: 742px; } .slide-3 { top: 1444px; }
  .slide-4 { top: 2146px; } .slide-5 { top: 2848px; } .slide-6 { top: 3550px; }

  .brand {
    position: absolute; top: 48px; right: 40px; z-index: 5; display: flex; align-items: center; gap: 8px;
    font-family: "Abril Fatface", Georgia, serif; font-size: 15px; color: var(--ink); white-space: nowrap;
  }
  .brand-dot { width: 22px; height: 22px; border-radius: 50%; background: var(--accent-red); }

  .slide-title { position: absolute; left: 40px; top: 48px; font-size: 44px; color: var(--ink); letter-spacing: .5px; }
  .slide-title .hl { color: var(--teal); }
  .body-copy { font-size: 15px; line-height: 1.45; color: var(--text); }

  /* Cover */
  .cover-title { position: absolute; left: 48px; top: 150px; font-size: 70px; line-height: 1.02; color: var(--ink); z-index: 2; }
  .cover-title .hl { color: var(--teal); }
  .cover-copy { position: absolute; left: 48px; top: 330px; width: 470px; }
  .cover-rings { position: absolute; left: 550px; top: 0; z-index: 1; }

  /* Agenda */
  .agenda-photo { position: absolute; left: 0; top: 40px; }
  .agenda-heading { position: absolute; left: 48px; top: 40px; font-size: 48px; color: var(--teal); }
  .agenda-list { position: absolute; left: 560px; top: 160px; list-style: none; }
  .agenda-list li { display: flex; align-items: center; gap: 14px; height: 90px; font-size: 30px; color: var(--ink); }
  .agenda-bullet { width: 30px; height: 30px; border-radius: 50%; background: var(--teal-mist); border: 3px solid var(--accent-red); }

  /* Technical training */
  .ring { position: absolute; text-align: center; }
  .ring svg { display: block; margin: 0 auto; }
  .ring-label { font-family: "Abril Fatface", Georgia, serif; font-size: 24px; color: var(--ink); margin-top: 6px; white-space: nowrap; }
  .ring-value { position: absolute; left: 0; right: 0; top: 48px; font-family: "Abril Fatface", Georgia, serif; font-size: 36px; color: var(--ink); }
  .ring-icon { position: absolute; left: 50%; top: 100px; width: 22px; height: 22px; margin-left: -11px; border-radius: 50%; background: var(--accent-red); }
  .tech-copy { position: absolute; left: 660px; top: 140px; width: 420px; }
  .tech-copy p + p { margin-top: 22px; }

  /* KPI */
  .kpi-chart { position: absolute; left: 60px; top: 120px; }
  .kpi-list { position: absolute; left: 740px; top: 120px; list-style: none; }
  .kpi-list li { display: flex; align-items: flex-start; gap: 10px; height: 62px; }
  .kpi-dot { width: 9px; height: 9px; border-radius: 50%; margin-top: 12px; }
  .kpi-day { font-family: "Abril Fatface", Georgia, serif; font-size: 24px; color: var(--ink); width: 78px; }
  .kpi-note { font-size: 13px; line-height: 1.35; width: 230px; }

  /* Quality */
  .qa-copy { position: absolute; left: 40px; top: 140px; width: 580px; }
  .qa-copy p + p { margin-top: 26px; }
  .qa-pie { position: absolute; left: 660px; top: 90px; }

  /* Locations */
  .world-map { position: absolute; left: 0; top: 120px; width: 1120px; height: 390px; background: linear-gradient(180deg, var(--map), #bfbfbf); }
  .pin { position: absolute; display: flex; align-items: center; gap: 6px; font-family: "Abril Fatface", Georgia, serif; font-size: 26px; color: var(--ink); }
  .loc-copy { position: absolute; left: 40px; top: 540px; width: 1040px; font-family: "Abril Fatface", Georgia, serif; font-size: 16px; line-height: 1.45; color: var(--ink); }
</style>
</head>
<body>

<section class="slide slide-1">
  <div class="brand"><span class="brand-dot"></span>Dugout Caps Co.</div>
  <h1 class="cover-title display">Headwear<br><span class="hl">Manufacturing</span></h1>
  <p class="cover-copy body-copy">Lorem ipsum dolor sit amet, consectetur adipiscing elit, sed do eiusmod tempor incididunt ut labore et dolore magna aliqua. Quis ipsum suspendisse ultrices gravida. Risus commodo viverra maecenas accumsan lacus vel facilisis.</p>
  <svg class="cover-rings" width="380" height="380" viewBox="0 0 520 520">
    <circle cx="260" cy="260" r="250" fill="var(--teal-mist)"/>
    <circle cx="260" cy="260" r="210" fill="var(--teal-pale)"/>
    <circle cx="260" cy="260" r="170" fill="var(--teal-light)"/>
    <circle cx="260" cy="260" r="130" fill="var(--teal-mid)"/>
    <ellipse role="img" aria-label="Photo of a dark green batting helmet" cx="270" cy="260" rx="150" ry="120" fill="#1f5c48"/>
  </svg>
</section>

<section class="slide slide-2">
  <div class="brand"><span class="brand-dot"></span>Dugout Caps Co.</div>
  <svg class="agenda-photo" width="620" height="560" viewBox="0 0 620 560">
    <defs><linearGradient id="stadium" x1="0" y1="0" x2="0" y2="1"><stop offset="0" stop-color="#0b0f14"/><stop offset=".75" stop-color="#1d2a2c"/><stop offset="1" stop-color="#6b5a3e"/></linearGradient></defs>
    <polygon role="img" aria-label="Photo of a baseball batter swinging in a night stadium" points="0,0 620,0 450,560 0,560" fill="url(#stadium)"/>
  </svg>
  <h2 class="agenda-heading display">AGENDA</h2>
  <ul class="agenda-list display">
    <li><span class="agenda-bullet"></span>Technical Training</li>
    <li><span class="agenda-bullet"></span>KPI Reports</li>
    <li><span class="agenda-bullet"></span>Quality Assurance Training</li>
    <li><span class="agenda-bullet"></span>Locations</li>
  </ul>
</section>

<section class="slide slide-3">
  <div class="brand"><span class="brand-dot"></span>Dugout Caps Co.</div>
  <h2 class="slide-title display">TECHNICAL TRAINING</h2>
  <div class="ring" style="left:60px; top:140px; width:240px;">
    <svg width="170" height="170" viewBox="0 0 170 170"><circle cx="85" cy="85" r="74" fill="none" stroke="var(--track)" stroke-width="12"/><circle cx="85" cy="85" r="74" fill="none" stroke="var(--teal)" stroke-width="12" stroke-dasharray="241.8 465" transform="rotate(-90 85 85)"/></svg>
    <div class="ring-value">52%</div><span class="ring-icon"></span>
    <div class="ring-label">Parsonal Training</div>
  </div>
  <div class="ring" style="left:400px; top:140px; width:240px;">
    <svg width="170" height="170" viewBox="0 0 170 170"><circle cx="85" cy="85" r="74" fill="none" stroke="var(--track)" stroke-width="12"/><circle cx="85" cy="85" r="74" fill="none" stroke="var(--teal)" stroke-width="12" stroke-dasharray="302.2 465" transform="rotate(-90 85 85)"/></svg>
    <div class="ring-value">65%</div><span class="ring-icon"></span>
    <div class="ring-label">Online Training</div>
  </div>
  <div class="ring" style="left:140px; top:375px; width:240px;">
    <svg width="170" height="170" viewBox="0 0 170 170"><circle cx="85" cy="85" r="74" fill="none" stroke="var(--track)" stroke-width="12"/><circle cx="85" cy="85" r="74" fill="none" stroke="var(--teal)" stroke-width="12" stroke-dasharray="395.2 465" transform="rotate(-90 85 85)"/></svg>
    <div class="ring-value">85%</div><span class="ring-icon"></span>
    <div class="ring-label">Parsonal Training</div>
  </div>
  <div class="tech-copy body-copy">
    <p>Lorem ipsum dolor sit amet, consectetur adipiscing elit, sed do eiusmod tempor incididunt ut labore et dolore magna aliqua. Quis ipsum suspendisse ultrices gravida. Risus commodo viverra maecenas accumsan lacus vel facilisis. Lorem ipsum dolor sit amet, consectetur adipiscing elit, sed do eiusmod tempor incididunt ut labore et dolore magna aliqua.</p>
    <p>Lorem ipsum dolor sit amet, consectetur adipiscing elit, sed do eiusmod tempor incididunt ut labore et dolore magna aliqua. Quis ipsum suspendisse ultrices gravida. Risus commodo viverra maecenas accumsan lacus vel facilisis. Lorem ipsum dolor sit amet, consectetur adipiscing elit, sed do eiusmod tempor incididunt.</p>
  </div>
</section>

<section class="slide slide-4">
  <div class="brand"><span class="brand-dot"></span>Dugout Caps Co.</div>
  <h2 class="slide-title display">KPI <span class="hl">REPORTS</span></h2>
  <svg class="kpi-chart" width="560" height="340" viewBox="0 0 560 340" font-family="Josefin Sans, sans-serif" font-size="12" fill="#222">
    <rect x="0" y="0" width="560" height="330" fill="none" stroke="#dddddd"/>
    <line x1="10" y1="322" x2="550" y2="322" stroke="#999"/>
    <rect x="20" y="210" width="66" height="112" fill="var(--teal)"/>
    <rect x="94" y="178" width="66" height="144" fill="var(--brown)"/>
    <rect x="168" y="150" width="66" height="172" fill="var(--charcoal)"/>
    <rect x="242" y="118" width="66" height="204" fill="var(--sand)"/>
    <rect x="316" y="88" width="66" height="234" fill="var(--brown)"/>
    <rect x="390" y="70" width="66" height="252" fill="var(--sienna)"/>
    <rect x="464" y="50" width="66" height="272" fill="var(--slate)"/>
    <g text-anchor="middle">
      <text x="53" y="188">Day1</text><text x="127" y="156">Day2</text><text x="201" y="128">Day3</text>
      <text x="275" y="96">Day4</text><text x="349" y="66">Day5</text><text x="423" y="48">Day6</text><text x="497" y="28">Day7</text>
    </g>
  </svg>
  <ul class="kpi-list">
    <li><span class="kpi-dot" style="background:var(--teal)"></span><span class="kpi-day">Day1</span><span class="kpi-note">Lorem ipsum dolor sit amet, consectetur adipiscing elit.</span></li>
    <li><span class="kpi-dot" style="background:var(--brown)"></span><span class="kpi-day">Day2</span><span class="kpi-note">Lorem ipsum dolor sit amet, consectetur adipiscing elit.</span></li>
    <li><span class="kpi-dot" style="background:var(--charcoal)"></span><span class="kpi-day">Day3</span><span class="kpi-note">Lorem ipsum dolor sit amet, consectetur adipiscing elit.</span></li>
    <li><span class="kpi-dot" style="background:var(--sand)"></span><span class="kpi-day">Day4</span><span class="kpi-note">Lorem ipsum dolor sit amet, consectetur adipiscing elit.</span></li>
    <li><span class="kpi-dot" style="background:var(--brown)"></span><span class="kpi-day">Day5</span><span class="kpi-note">Lorem ipsum dolor sit amet, consectetur adipiscing elit.</span></li>
    <li><span class="kpi-dot" style="background:var(--sienna)"></span><span class="kpi-day">Day6</span><span class="kpi-note">Lorem ipsum dolor sit amet, consectetur adipiscing elit.</span></li>
    <li><span class="kpi-dot" style="background:var(--slate)"></span><span class="kpi-day">Day7</span><span class="kpi-note">Lorem ipsum dolor sit amet, consectetur adipiscing elit.</span></li>
  </ul>
</section>

<section class="slide slide-5">
  <div class="brand"><span class="brand-dot"></span>Dugout Caps Co.</div>
  <h2 class="slide-title display">QUALITY ASSURANCE <span class="hl">TRAINING</span></h2>
  <div class="qa-copy body-copy">
    <p>Lorem ipsum dolor sit amet, consectetur adipiscing elit, sed do eiusmod tempor incididunt ut labore et dolore magna aliqua. Quis ipsum suspendisse ultrices gravida. Risus commodo viverra maecenas accumsan lacus vel facilisis. Lorem ipsum dolor sit amet, consectetur adipiscing elit, sed do eiusmod tempor incididunt ut labore et dolore magna aliqua. Quis ipsum suspendisse ultrices gravida. Risus commodo viverra maecenas accumsan lacus vel facilisis. Lorem ipsum dolor sit amet, consectetur adipiscing elit, sed do eiusmod tempor incididunt ut labore et dolore magna aliqua.</p>
    <p>Lorem ipsum dolor sit amet, consectetur adipiscing elit, sed do eiusmod tempor incididunt ut labore et dolore magna aliqua. Quis ipsum suspendisse ultrices gravida. Risus commodo viverra maecenas accumsan lacus vel facilisis. Lorem ipsum dolor sit amet, consectetur adipiscing elit, sed do eiusmod tempor incididunt ut labore et dolore magna aliqua.</p>
  </div>
  <svg class="qa-pie" width="520" height="520" viewBox="0 0 520 520" font-family="Abril Fatface, serif" fill="#fff">
    <circle cx="260" cy="260" r="240" fill="var(--teal)"/>
    <path d="M260 260 L260 20 A240 240 0 0 1 500 260 Z" fill="var(--sand)" stroke="#fff" stroke-width="4"/>
    <text x="345" y="170" font-size="40" text-anchor="middle">25%</text>
    <text x="345" y="194" font-size="12" font-family="Josefin Sans, sans-serif" text-anchor="middle">LOREM IPSUM</text>
    <text x="190" y="370" font-size="48" text-anchor="middle">75%</text>
    <text x="190" y="396" font-size="13" font-family="Josefin Sans, sans-serif" text-anchor="middle">LOREM IPSUM</text>
  </svg>
</section>

<section class="slide slide-6">
  <div class="brand"><span class="brand-dot"></span>Dugout Caps Co.</div>
  <h2 class="slide-title display">OUR <span class="hl">LOCATIONS</span></h2>
  <div class="world-map" role="img" aria-label="Grey world map showing factory locations"></div>
  <div class="pin" style="left:186px; top:250px;"><svg width="20" height="28" viewBox="0 0 20 28"><path d="M10 0a10 10 0 0 1 10 10c0 7-10 18-10 18S0 17 0 10A10 10 0 0 1 10 0z" fill="var(--accent-red)"/><circle cx="10" cy="10" r="4" fill="#fff"/></svg>Mexico</div>
  <div class="pin" style="left:776px; top:196px;"><svg width="20" height="28" viewBox="0 0 20 28"><path d="M10 0a10 10 0 0 1 10 10c0 7-10 18-10 18S0 17 0 10A10 10 0 0 1 10 0z" fill="var(--accent-red)"/><circle cx="10" cy="10" r="4" fill="#fff"/></svg>China</div>
  <div class="pin" style="left:738px; top:250px;"><svg width="20" height="28" viewBox="0 0 20 28"><path d="M10 0a10 10 0 0 1 10 10c0 7-10 18-10 18S0 17 0 10A10 10 0 0 1 10 0z" fill="var(--accent-red)"/><circle cx="10" cy="10" r="4" fill="#fff"/></svg>Bangladesh</div>
  <p class="loc-copy">Lorem ipsum dolor sit amet, consectetur adipiscing elit, sed do eiusmod tempor incididunt ut labore et dolore magna aliqua. Quis ipsum suspendisse ultrices gravida. Risus commodo viverra maecenas accumsan lacus vel facilisis.</p>
</section>

</body>
</html>
```